Bright Horizon Website

Bright Horizon Advisory Services is a company which provides specialised advise in carbon markets, climate policy, landscapes, resilience and change. We are based in Australia but the majority of our business is global. Our clients range from governments to large corporates and not for profit organisations.
Our focus is on developing the capabilities of government officials, business decision makers and land managers so they can better navigate the complexity of climate change and sustainability.
We are looking for a website that is consistent with the high end professional services which we provide to serious players.
I have attached two versions of our logo. I have also attached the back of our business card so you can get a sense of what we hand to potential clients.

Target Market(s)

Professional individuals, decision makers, board members etc, government officials.

Industry/Entity Type

Government

Number of Pages Required

4 page

Font styles to use
Serif
Sans Serif

Requirements
Must have
• Please provide
• 1. Home page
• 2. Service page template
• 3. Contact page
• 4. Lead expert profile page

```html
<!DOCTYPE html>
<html lang="en">
<head>
<meta charset="utf-8">
<title>Bright Horizon Advisory Services</title>
<link rel="stylesheet" href="https://fonts.googleapis.com/css2?family=Arimo:wght@400;700&family=Cormorant+Garamond:wght@500&display=swap">
<style>
:root{
  --accent:#ef4238;
  --ink:#4a4a4a;
  --muted:#777;
  --soft:#9a9a9a;
  --band:#f2f2f2;
  --rule:#d9d9d9;
  --white:#fff;
  --top:#3a3a3a;
}
*{box-sizing:border-box;margin:0;padding:0}
html,body{width:1200px;height:1021px;overflow:hidden;background:var(--white)}
body{font-family:"Arimo",Arial,sans-serif;color:var(--ink);position:relative}
.site-header{position:absolute;top:0;left:0;width:1200px;height:64px;border-top:2px solid var(--top);background:var(--white)}
.brand{position:absolute;left:268px;top:14px;display:flex;align-items:center;gap:10px}
.brand-dot{width:30px;height:30px;border-radius:50%;background:#8c8c8c}
.brand-name{font-family:"Cormorant Garamond",Georgia,serif;font-weight:500;font-size:21px;line-height:19px;letter-spacing:1.5px;color:#3b3b3b;text-transform:uppercase;width:110px}
.main-nav{position:absolute;top:0;left:0;width:1200px;height:62px;font-size:10px;color:var(--ink)}
.main-nav a{position:absolute;top:25px;color:inherit;text-decoration:none;white-space:nowrap}
.main-nav a.is-current{color:var(--accent)}
.main-nav a.is-current::before{content:"";position:absolute;top:-25px;left:0;right:0;height:2px;background:var(--accent)}
.nav-search{position:absolute;left:891px;top:24px;display:flex;align-items:center;gap:10px}
.nav-search .divider{width:1px;height:16px;background:var(--rule)}
.hero{position:absolute;top:64px;left:0;width:1200px;height:329px;background:radial-gradient(ellipse at 70% 40%,#6a5a40 0%,#3a3026 40%,#1e1a17 100%)}
.hero-copy{position:absolute;top:137px;left:0;width:1200px;text-align:center;color:var(--white)}
.hero-title{font-size:14.5px;font-weight:400;line-height:18px}
.hero-title em{font-style:normal;color:var(--accent)}
.hero-lead{margin-top:12px;font-size:9.5px;line-height:14px}
.intro{position:absolute;top:393px;left:0;width:1200px;height:108px;background:var(--band);text-align:center}
.intro-lead{margin-top:27px;font-size:9.5px;font-weight:700;color:var(--muted)}
.intro-lead a,.contact-band a{color:var(--accent)}
.intro-text{margin-top:11px;font-size:8px;line-height:14px;color:var(--muted)}
.engagements{position:absolute;top:501px;left:268px;width:643px;height:207px}
.section-title{position:absolute;top:44px;left:0;width:643px;text-align:center;font-size:10.5px;font-weight:400;color:var(--ink)}
.section-title::before,.section-title::after{content:"";position:absolute;top:6px;width:196px;height:3px;border-top:1px solid var(--rule);border-bottom:1px solid var(--rule)}
.section-title::before{left:0}
.section-title::after{right:0}
.service{position:absolute;top:92px;width:116px;margin-left:-58px;text-align:center;font-size:8.3px;line-height:14px;color:var(--ink)}
.service svg{display:block;margin:0 auto 8px;width:34px;height:34px}
.service.is-active{color:var(--accent)}
.contact-band{position:absolute;top:708px;left:0;width:1200px;height:89px;background:var(--band);text-align:center;padding-top:33px;font-size:9.8px;font-weight:700;line-height:14.5px;color:var(--muted)}
.testimonial{position:absolute;top:797px;left:0;width:1200px;text-align:center}
.quote-mark{margin-top:26px;font-family:Georgia,serif;font-size:30px;line-height:30px;color:#888}
.quote-text{margin:10px auto 0;width:510px;font-size:8px;line-height:14px;color:var(--soft)}
.quote-author{margin-top:20px;font-size:8.5px;font-weight:700;color:var(--accent)}
.quote-date{margin-top:5px;font-size:6.5px;color:var(--soft)}
.site-footer{position:absolute;top:981px;left:0;width:1200px;height:40px;border-top:1px solid var(--rule);text-align:center;padding-top:17px;font-size:7px;color:var(--soft)}
</style>
</head>
<body>
<header class="site-header">
  <div class="brand"><span class="brand-dot"></span><span class="brand-name">Bright Horizon</span></div>
  <nav class="main-nav">
    <a class="is-current" href="#" style="left:605px">Home</a>
    <a href="#" style="left:670px">Services</a>
    <a href="#" style="left:741px">Lead Expert</a>
    <a href="#" style="left:824px">Contact Us</a>
  </nav>
  <div class="nav-search"><span class="divider"></span>
    <svg width="12" height="12" viewBox="0 0 12 12"><circle cx="4.5" cy="4.5" r="3.3" fill="none" stroke="#888" stroke-width="1.3"/><line x1="7" y1="7" x2="11" y2="11" stroke="#888" stroke-width="1.8"/></svg>
  </div>
</header>

<section class="hero" role="img" aria-label="Dim desk scene with a notebook, pen, phone and tablet">
  <div class="hero-copy">
    <h1 class="hero-title">Bright Horizon provides expert advisory services<br>in <em>carbon markets, climate policy, landscapes and change</em>.</h1>
    <p class="hero-lead">Our focus is on developing the capabilities of government officials, business decision makers and land managers<br>so they can better navigate the complexity of climate change &amp; sustainability.</p>
  </div>
</section>

<section class="intro">
  <p class="intro-lead">Daniel Marsh leads all of Bright Horizon's advisory engagements.&nbsp; His profile is available <a href="#">Click Here</a>.</p>
  <p class="intro-text">We provide advisory services across a number of specialised areas.&nbsp; However, all of our advisory services<br>are tailored to the situation and needs of the client, so no two engagements are the same</p>
</section>

<section class="engagements">
  <h2 class="section-title">A selection of recent engagements is provided</h2>
  <div class="service" style="left:37px">
    <svg viewBox="0 0 36 36" fill="#6b6b6b" stroke="#6b6b6b" stroke-width="2"><line x1="18" y1="18" x2="8" y2="6"/><line x1="18" y1="18" x2="30" y2="8"/><line x1="18" y1="18" x2="6" y2="26"/><line x1="18" y1="18" x2="28" y2="30"/><circle cx="18" cy="18" r="5" stroke="none"/><circle cx="8" cy="6" r="3.5" stroke="none"/><circle cx="30" cy="8" r="3.5" stroke="none"/><circle cx="6" cy="26" r="3.5" stroke="none"/><circle cx="28" cy="30" r="3.5" stroke="none"/></svg>
    Corporate Advisory on<br>Carbon Markets</div>
  <div class="service is-active" style="left:151px">
    <svg viewBox="0 0 36 36" fill="none" stroke="#ef4238" stroke-width="3"><rect x="3" y="4" width="30" height="20" rx="2"/><line x1="18" y1="25" x2="18" y2="30"/><line x1="11" y1="31" x2="25" y2="31"/></svg>
    Project Mechanisms</div>
  <div class="service" style="left:262px">
    <svg viewBox="0 0 36 36" fill="none" stroke="#6b6b6b" stroke-width="2.5"><circle cx="14" cy="14" r="10"/><line x1="14" y1="9" x2="14" y2="19"/><line x1="9" y1="14" x2="19" y2="14"/><line x1="22" y1="22" x2="32" y2="32" stroke-width="4"/></svg>
    Monitoring,<br>Reporting &amp; Verification</div>
  <div class="service" style="left:380px">
    <svg viewBox="0 0 36 36" fill="none" stroke="#6b6b6b" stroke-width="2.5"><circle cx="18" cy="18" r="14"/><polyline points="18,9 18,18 24,21"/></svg>
    Institutional Arrangements</div>
  <div class="service" style="left:494px">
    <svg viewBox="0 0 36 36" fill="none" stroke="#6b6b6b"><circle cx="13" cy="21" r="7" stroke-width="5" stroke-dasharray="3 2.5"/><circle cx="13" cy="21" r="3" stroke-width="2"/><circle cx="26" cy="11" r="5" stroke-width="4" stroke-dasharray="2.5 2"/><circle cx="26" cy="11" r="2" stroke-width="1.5"/></svg>
    Training &amp; Coaching</div>
  <div class="service" style="left:600px">
    <svg viewBox="0 0 36 36" fill="none" stroke="#6b6b6b" stroke-width="3.5" stroke-linecap="round"><line x1="8" y1="28" x2="26" y2="10"/><circle cx="28" cy="8" r="4" stroke-width="2.5"/><line x1="8" y1="8" x2="28" y2="28"/><line x1="5" y1="5" x2="10" y2="10" stroke-width="2"/></svg>
    China's Carbon Markets</div>
</section>

<section class="contact-band">
  Please <a href="#">Contact us</a> if you would like to explore how Bright Horizon<br>can support your efforts in climate change &amp; sustainability.
</section>

<section class="testimonial">
  <div class="quote-mark">&ldquo;</div>
  <p class="quote-text">I love the theatre tonic over the counter substitute Though Harlow felt his ball had only oscillated before he ran up a double-bogey six there, video footage later showed that it had slightly shifted its position and his score was amended to a quadruple bogey eight.</p>
  <p class="quote-author">Margaret</p>
  <p class="quote-date">October 19, 2014 at 5:08 pm</p>
</section>

<footer class="site-footer">Copyright All Right Reserved 2014.</footer>
</body>
</html>
```